Updated Business Cards

We need to update our business cards to reflect new services and employees. We are a luxury vacation rental company in Sandpoint, Idaho. Would also like to make the front facing font easier to read (larger fonts) I love the original logo created for our company and want to use this for the back of the business card created like before - with the dark blue color. See previous files.

Front of the card needs to include:
Employee Name
Title
Phone: 208-555-0147 (ext X)
Address: 418 W. Larkmoor St, Ste 5
Lake Vireo, MT 83871
Book Direct: www.RestWillowbay.example

```html
<!DOCTYPE html>
<html lang="en">
<head>
<meta charset="utf-8">
<title>Halvorsen Management – Business Cards</title>
<link rel="stylesheet" href="https://fonts.googleapis.com/css2?family=Noto+Serif:wght@400;500;600;700&display=swap">
<style>
  :root {
    --stage: #1c1c1e;
    --blue-light: #29a9e2;
    --blue-deep: #1a7cc2;
    --navy: #232a6b;
    --graphite: #4a4a4c;
    --white: #ffffff;
    --serif: "Noto Serif", Georgia, serif;
  }
  * { box-sizing: border-box; margin: 0; padding: 0; }
  html, body { width: 1200px; height: 1000px; overflow: hidden; }
  body { background: var(--stage); font-family: var(--serif); color: var(--white); position: relative; }

  .card {
    position: absolute; left: 222px; width: 756px; height: 432px;
    border-radius: 30px; overflow: hidden;
    background: radial-gradient(ellipse at 50% 50%, var(--blue-light) 0%, #23a0dc 45%, var(--blue-deep) 100%);
  }
  .card--front { top: 60px; }
  .card--back { top: 510px; height: 430px; }

  .tab-top {
    position: absolute; left: 349px; top: 0; width: 59px; height: 47px;
    background: var(--navy); border-radius: 0 0 30px 30px;
  }
  .spine {
    position: absolute; left: 349px; bottom: 0; width: 59px;
    background: var(--graphite); border-radius: 30px 30px 0 0;
  }
  .card--front .spine { height: 252px; }
  .card--back .spine { height: 195px; }

  .brand {
    position: absolute; left: 0; right: 0; display: flex; justify-content: center; align-items: center;
    gap: 12px; color: var(--navy); font-weight: 700; letter-spacing: 0.5px;
  }
  .brand__dot { border-radius: 50%; background: var(--navy); }
  .card--front .brand { top: 106px; font-size: 27px; }
  .card--front .brand__dot { width: 22px; height: 22px; }
  .card--back .brand { top: 150px; font-size: 44px; }
  .card--back .brand__dot { width: 34px; height: 34px; }

  .person { position: absolute; right: 425px; top: 286px; text-align: right; }
  .person__name { font-size: 34px; font-weight: 600; line-height: 1.1; }
  .person__title { font-size: 19px; font-weight: 500; margin-top: 4px; }

  .icon { position: absolute; left: 366px; width: 24px; height: 24px; }
  .icon svg { width: 24px; height: 24px; display: block; }

  .contact { position: absolute; left: 424px; font-size: 18px; font-weight: 500; line-height: 30px; white-space: nowrap; }
  .contact--phone { top: 212px; font-size: 22px; }
  .contact--email { top: 254px; }
  .contact--web { top: 297px; }
  .contact--address { top: 342px; }
</style>
</head>
<body>
  <section class="card card--front" aria-label="Card front">
    <div class="tab-top"></div>
    <div class="brand"><span class="brand__dot"></span>Halvorsen Management</div>

    <div class="person">
      <p class="person__name">Marcus Ellery</p>
      <p class="person__title">Managing Director</p>
    </div>

    <div class="spine"></div>
    <span class="icon" style="top:218px">
      <svg viewBox="0 0 24 24" fill="none" stroke="#fff" stroke-width="2" stroke-linecap="round"><path d="M5 3h4l2 5-2.5 1.5a11 11 0 0 0 6 6L16 13l5 2v4a2 2 0 0 1-2 2A16 16 0 0 1 3 5a2 2 0 0 1 2-2z"/><path d="M15 3a6 6 0 0 1 6 6M15 7a2 2 0 0 1 2 2"/></svg>
    </span>
    <span class="icon" style="top:259px">
      <svg viewBox="0 0 24 24"><rect x="2" y="5" width="20" height="14" rx="1.5" fill="#fff"/><path d="M2.5 6l9.5 7 9.5-7" fill="none" stroke="#4a4a4c" stroke-width="1.6"/></svg>
    </span>
    <span class="icon" style="top:303px">
      <svg viewBox="0 0 24 24" fill="none" stroke="#fff" stroke-width="1.8"><circle cx="11" cy="11" r="9"/><path d="M2 11h18M11 2c3 3 3 15 0 18M11 2c-3 3-3 15 0 18"/><path d="M15 15l7 3-3 1-1 3z" fill="#fff"/></svg>
    </span>
    <span class="icon" style="top:362px">
      <svg viewBox="0 0 24 24"><path d="M12 1a8 8 0 0 0-8 8c0 6 8 14 8 14s8-8 8-14a8 8 0 0 0-8-8z" fill="#fff"/><circle cx="12" cy="9" r="3" fill="#4a4a4c"/></svg>
    </span>

    <p class="contact contact--phone">208-555-0147</p>
    <p class="contact contact--email">hello@restwillowbay.example</p>
    <p class="contact contact--web">www.RestWillowbay.example</p>
    <p class="contact contact--address">418 W. Larkmoor St, Ste 5<br>Lake Vireo, MT 83871</p>
  </section>

  <section class="card card--back" aria-label="Card back">
    <div class="tab-top"></div>
    <div class="brand"><span class="brand__dot"></span>Halvorsen Management</div>
    <div class="spine"></div>
  </section>
</body>
</html>
```